Create a Brochure Design for Brantley Homecare

Brantley Homecare is a subsidiary of the Brantley Care Group. This brochure is specifically for the Brantley Homecare company and brand. Create a 3 panel, A4, front and back, tri-fold brochure. This brochure will be a way to introduce our Homecare services to the community, prospective clients, and various referral partners. The brochure must be eye catching, unique in its deliverables and demonstrate both attention to detail and comfort. Our organization is sophisticated and built around warmth, care and individualized personal attention. The most important aspect of this design is to focus on creating a nurturing, warm, and inviting feel where you would want to have a Nurse or Nurse’s Aide in your own home or a loved one’s home.

I am open to the creativity of the designer to develop something based on the above criteria; however I would like the design to work well with the existing collateral material. What I mean by that is that while I want everything to have its own personality and stand out as its own brand representative, I still need to be able to tell that the overall design concept stays stylistically inside of the same ‘family’ of existing designed material. Because of this, below I would like for the designer to pull inspiration from the link to our website (Located below) as well as from the attachment of our recently refreshed business cards (Attached). This should allow each design to be unique and creative, while still staying inside of a framework and the feel/style that I am looking for.

Finally, I want all the designers to understand that this brochure design is for a private, in home, healthcare company where we are responsible for providing personalized care for a culturally and ethnically diverse make-up clientele of all ages. The photos that are used must represent an image of warmth, care, and a positive interaction between client and caregiver.

Look under the Brantley Homecare tab at www.brantleycaregroup-example.net

Industry/Entity Type

Healthcare

Requirements
Must have
• • The Brantley Homecare company logo must be included.

```html
<!DOCTYPE html>
<html lang="en">
<head>
<meta charset="utf-8">
<title>Brantley Homecare – Tri-fold Brochure</title>
<link rel="stylesheet" href="https://fonts.googleapis.com/css2?family=Arimo:wght@400;700&family=Oswald:wght@500&family=Gochi+Hand&display=swap">
<style>
  :root {
    --green-dark: #0d7a3e;
    --green-deep: #0a6a35;
    --lime: #c6dc5e;
    --lime-soft: #dfeb9a;
    --lime-pale: #eef5c8;
    --salmon: #e8907a;
    --ink: #3a3a3a;
    --white: #ffffff;
    --canvas: #f3f3ef;
  }
  * { box-sizing: border-box; margin: 0; padding: 0; }
  html, body { width: 1200px; height: 750px; overflow: hidden; }
  body {
    background: var(--canvas);
    font-family: "Arimo", Arial, sans-serif;
    color: var(--ink);
    position: relative;
  }
  .panel {
    position: absolute;
    top: 105px;
    height: 540px;
    background: var(--white);
    overflow: hidden;
  }
  /* ---------- Panel: Types of Service ---------- */
  .services { left: 80px; width: 250px; background: var(--lime); }
  .services__title {
    position: absolute; left: 22px; top: 14px;
    font-family: "Oswald", "Arial Narrow", sans-serif;
    line-height: 0.95; text-transform: uppercase;
  }
  .services__title .small { display: block; color: var(--white); font-size: 19px; }
  .services__title .big { display: block; color: var(--green-dark); font-size: 33px; }
  .services__body-shape { position: absolute; left: 0; top: 68px; }
  .services__body {
    position: absolute; left: 22px; right: 14px; top: 94px;
    color: var(--white); font-size: 8.6px; line-height: 1.28;
  }
  .services__body h2 { font-size: 10.5px; color: var(--lime-soft); margin-bottom: 7px; }
  .services__body h2 span { font-weight: 400; color: var(--white); }
  .services__body h3 { font-size: 9.2px; color: var(--lime); margin: 8px 0 2px; font-weight: 700; }
  .services__body .note { font-size: 6.8px; font-style: italic; margin-top: 4px; }
  .services__body ul { list-style: none; margin-top: 5px; }
  .services__body li { position: relative; padding-left: 10px; margin-bottom: 2.5px; }
  .services__body li::before { content: "•"; position: absolute; left: 0; }
  .services__body li small { display: block; font-size: 7px; line-height: 1.2; }
  .services__call {
    position: absolute; left: 0; right: 0; bottom: 8px;
    text-align: center; color: var(--green-deep); font-size: 10px; line-height: 1.25;
  }
  .services__call strong { font-size: 16px; }

  /* ---------- Spread: Transportation / Medication ---------- */
  .spread { left: 330px; width: 500px; }
  .spread__fold { position: absolute; left: 250px; top: 0; bottom: 0; border-left: 1px dashed #cfcfcf; }
  .quote-band { position: absolute; left: 0; top: 0; }
  .quote {
    position: absolute; left: 66px; right: 26px; top: 34px;
    font-family: "Gochi Hand", cursive; color: var(--green-dark);
    font-size: 15px; line-height: 1.25;
  }
  .quote-mark {
    position: absolute; left: 20px; top: 10px;
    font-family: Georgia, serif; font-size: 80px; line-height: 1; color: var(--white);
  }
  .photo { position: absolute; top: 112px; height: 138px; }
  .photo--exercise { left: 0; width: 118px; background: linear-gradient(135deg, #c9a98b, #e8d9c8 55%, #b74a4a); }
  .photo--stethoscope { left: 124px; width: 178px; background: linear-gradient(160deg, #6fa6cf, #2f6fa6 60%, #1d4b78); }
  .photo--meal { left: 308px; width: 192px; background: linear-gradient(135deg, #d8c5a8, #f0e4d2 50%, #d94d6e); }
  .photo-curve { position: absolute; left: 0; top: 218px; }
  .info { position: absolute; top: 268px; width: 250px; padding: 0 22px; font-size: 8.8px; line-height: 1.33; }
  .info--transport { left: 0; }
  .info--medication { left: 250px; }
  .info h3 {
    color: var(--green-dark); font-size: 10px; line-height: 1.2; min-height: 26px;
    display: flex; align-items: flex-end; padding-bottom: 4px;
  }
  .info__rule { position: absolute; left: 0; width: 500px; top: 296px; border-top: 1px solid var(--lime); }
  .info p { margin-top: 6px; }
  .spread__foot { position: absolute; left: 0; bottom: 0; }

  /* ---------- Front cover ---------- */
  .cover { left: 870px; width: 250px; }
  .cover__photo {
    position: absolute; left: 0; top: 0; width: 250px; height: 290px;
    background: linear-gradient(160deg, #e9d3c0 0%, #c99f86 35%, #8fc2d8 70%, #bfe0ec 100%);
  }
  .cover__brand { position: absolute; left: 0; right: 0; top: 318px; text-align: center; }
  .cover__mark { width: 24px; height: 24px; background: var(--salmon); margin: 0 auto 10px; }
  .cover__name { font-size: 22px; font-weight: 700; color: var(--green-dark); line-height: 1.1; }
  .cover__tagline { margin-top: 8px; font-size: 9px; color: var(--salmon); }
  .cover__swoosh { position: absolute; left: 0; bottom: 0; }
</style>
</head>
<body>

<!-- Inside left panel -->
<section class="panel services">
  <h1 class="services__title"><span class="small">Types of</span><span class="big">Service</span></h1>
  <svg class="services__body-shape" width="250" height="420" viewBox="0 0 250 420" aria-hidden="true">
    <path d="M0 18 Q120 -8 250 6 L250 402 L0 404 Z" fill="var(--green-dark)"/>
  </svg>
  <div class="services__body">
    <h2>Brantley Homecare Team <span>includes:</span></h2>
    <h3>Home Assistants*</h3>
    <p>Will provide companionship, assist with meal preparation, and light housekeeping (dusting, vacuuming, mopping, sweeping, bathroom and kitchen clean up, linen change and laundry).</p>
    <p class="note">*No heavy cleaning. No hands-on assistance.</p>
    <h3>Nurses Aide/Assistants*</h3>
    <p>Help with all the same services as Home Assistants but they’ll also help with personal care:</p>
    <ul>
      <li>Bathing</li>
      <li>Toileting</li>
      <li>Incontinent care</li>
      <li>Dressing</li>
      <li>Transferring the client from bed, bath or car</li>
      <li>Range of motion exercises</li>
      <li>Turning and positioning</li>
      <li>Assistance with a wheelchair or walker<small>(This level of care is appropriate for patients with Alzheimer’s and Dementia)</small></li>
    </ul>
    <p class="note">*No heavy cleaning.</p>
    <h3>Skilled Nurses</h3>
    <p>We offer a wide range of skilled nursing services ranging from Licensed Practical Nurses (LPN) to Registered Nurses (RN).</p>
  </div>
  <p class="services__call">Call <strong>808-555-0172</strong><br>to discuss your needs further.</p>
</section>

<!-- Inside centre and right panels -->
<section class="panel spread">
  <svg class="quote-band" width="500" height="150" viewBox="0 0 500 150" aria-hidden="true">
    <path d="M0 0 H500 V92 Q250 150 0 112 Z" fill="var(--lime-soft)"/>
  </svg>
  <span class="quote-mark">&ldquo;</span>
  <p class="quote">This is more than a job for us. Some people devote their lives to teaching, some to science. For us, it’s caring for you or your family member. Our job is simply to make your job easier.”</p>

  <div class="photo photo--exercise" role="img" aria-label="Photo: caregiver helping a smiling senior man with light exercise"></div>
  <div class="photo photo--stethoscope" role="img" aria-label="Photo: stethoscope resting on folded blue scrubs"></div>
  <div class="photo photo--meal" role="img" aria-label="Photo: nurse serving a meal tray to a senior woman"></div>
  <svg class="photo-curve" width="500" height="50" viewBox="0 0 500 50" aria-hidden="true">
    <path d="M0 20 Q250 60 500 0 V14 Q250 70 0 36 Z" fill="var(--salmon)"/>
    <path d="M0 36 Q250 70 500 14 V50 H0 Z" fill="var(--white)"/>
  </svg>

  <div class="info__rule"></div>
  <article class="info info--transport">
    <h3>Transportation Services / Escort &amp; Errand Services:</h3>
    <p>If a <strong>Brantley Homecare</strong> client who already is receiving personal care services requests that our caregiver provide escort or errand services, such as grocery shopping, appointments, errands or outings, there will be an additional fee assessed to the client. Clients who prefer not to pay for these additional charges may choose to take alternate means, such as using their own vehicle (with caregiver driving) or using public transportation, such as a bus or taxi.</p>
  </article>
  <article class="info info--medication">
    <h3>Medication Services:</h3>
    <p><strong>Brantley Homecare</strong> clients who already receive personal care services may choose the services of a Licensed Nurse to pre-pour medications. A licensed nurse will pre-pour a client’s medication in weekly pill containers for a 28-day period. A list of medications including over-the-counter medications will be provided to the nurse by the client or family before each visit.</p>
  </article>

  <svg class="spread__foot" width="500" height="60" viewBox="0 0 500 60" aria-hidden="true">
    <path d="M0 60 V40 Q120 10 260 30 Q380 48 500 20 V60 Z" fill="var(--lime-pale)"/>
  </svg>
  <div class="spread__fold"></div>
</section>

<!-- Front cover -->
<section class="panel cover">
  <div class="cover__photo" role="img" aria-label="Photo: caregiver's hands gently holding an elderly client's hands on a blue blanket"></div>
  <div class="cover__brand">
    <div class="cover__mark"></div>
    <p class="cover__name">Brantley Homecare</p>
    <p class="cover__tagline">Someone you can depend on... Without question.</p>
  </div>
  <svg class="cover__swoosh" width="250" height="140" viewBox="0 0 250 140" aria-hidden="true">
    <defs>
      <linearGradient id="swooshGreen" x1="0" y1="0" x2="1" y2="0">
        <stop offset="0" stop-color="var(--lime-pale)"/>
        <stop offset="1" stop-color="var(--lime)"/>
      </linearGradient>
    </defs>
    <path d="M0 70 Q130 30 250 40 V140 H0 Z" fill="url(#swooshGreen)"/>
    <path d="M0 92 Q130 60 250 66 V140 H0 Z" fill="var(--white)"/>
    <path d="M0 102 Q130 74 250 78 V140 H0 Z" fill="var(--salmon)"/>
  </svg>
</section>

</body>
</html>
```